Criação de Papelaria Profissional para Consultoria de Negócios
A empresa queria:
" Consultoria em planejamento estratégico... marketing... aulas.. palestras.. artigos e livros publicados "

```html
<!DOCTYPE html>
<html lang="pt-BR">
<head>
<meta charset="UTF-8">
<title>Cartão de Visita – Rafael Moreira Consultoria</title>
<link rel="stylesheet" href="https://fonts.googleapis.com/css2?family=Open+Sans:wght@400;600&display=swap">
<style>
  :root {
    --page-bg: #e9e7e3;
    --card-dark: #2a2a2a;
    --card-light: #ffffff;
    --accent: #f05a1e;
    --ink: #333333;
    --ink-soft: #555555;
    --rule-light: #f2f2f2;
  }
  html, body {
    margin: 0;
    padding: 0;
    width: 1200px;
    height: 1200px;
    overflow: hidden;
    background: var(--page-bg);
    font-family: "Open Sans", Arial, sans-serif;
  }
  .stage {
    position: relative;
    width: 1200px;
    height: 1200px;
  }
  .card {
    position: absolute;
    left: 288px;
    width: 624px;
    height: 348px;
    box-shadow: 0 6px 18px rgba(0,0,0,0.18);
    overflow: hidden;
  }
  .card-front { top: 228px; background: var(--card-dark); }
  .card-back  { top: 636px; background: var(--card-light); }
  .card-bands {
    position: absolute;
    inset: 0;
    width: 100%;
    height: 100%;
  }
  .brand-name {
    position: absolute;
    white-space: nowrap;
    font-weight: 400;
    letter-spacing: 1px;
    text-transform: uppercase;
    display: flex;
    align-items: center;
    gap: 12px;
  }
  .brand-mark {
    width: 12px;
    height: 12px;
    background: var(--accent);
  }
  .card-front .brand-name {
    left: 50%;
    top: 186px;
    transform: translateX(-50%);
    color: #ffffff;
    font-size: 26px;
  }
  .card-back .brand-name {
    left: 340px;
    top: 212px;
    color: var(--ink);
    font-size: 22px;
  }
  .holder-name {
    position: absolute;
    left: 32px;
    top: 58px;
    margin: 0;
    font-size: 26px;
    font-weight: 400;
    color: var(--ink);
  }
  .holder-role {
    position: absolute;
    left: 32px;
    top: 92px;
    margin: 0;
    font-size: 18px;
    color: var(--ink-soft);
  }
  .contact-list {
    position: absolute;
    left: 36px;
    top: 140px;
    margin: 0;
    padding: 0;
    list-style: none;
  }
  .contact-item {
    position: absolute;
    left: 0;
    display: flex;
    align-items: center;
    gap: 12px;
    font-size: 15px;
    line-height: 19px;
    color: var(--ink-soft);
    white-space: nowrap;
  }
  .contact-item.is-web   { top: 0; }
  .contact-item.is-phone { top: 62px; }
  .contact-item.is-place { top: 134px; }
  .contact-icon {
    width: 28px;
    height: 28px;
    flex: none;
  }
</style>
</head>
<body>
<main class="stage">

  <section class="card card-front" aria-label="Frente do cartão">
    <svg class="card-bands" viewBox="0 0 624 348" aria-hidden="true">
      <polygon points="0,0 470,0 458,10 0,10" fill="var(--accent)"/>
      <polygon points="478,0 624,0 624,10 466,10" fill="var(--rule-light)"/>
      <polygon points="0,338 190,338 202,348 0,348" fill="var(--rule-light)"/>
      <polygon points="196,338 624,338 624,348 208,348" fill="var(--accent)"/>
    </svg>
    <div class="brand-name"><span class="brand-mark"></span>Rafael Moreira</div>
  </section>

  <section class="card card-back" aria-label="Verso do cartão">
    <svg class="card-bands" viewBox="0 0 624 348" aria-hidden="true">
      <polygon points="0,0 420,0 408,10 0,10" fill="var(--accent)"/>
      <polygon points="428,0 624,0 624,10 416,10" fill="var(--card-dark)"/>
      <polygon points="0,338 120,338 132,348 0,348" fill="var(--card-dark)"/>
      <polygon points="126,338 624,338 624,348 138,348" fill="var(--accent)"/>
    </svg>

    <h2 class="holder-name">Nome Completo</h2>
    <p class="holder-role">Cargo</p>

    <ul class="contact-list">
      <li class="contact-item is-web">
        <svg class="contact-icon" viewBox="0 0 28 28" aria-hidden="true">
          <circle cx="14" cy="14" r="14" fill="var(--accent)"/>
          <circle cx="14" cy="14" r="7" fill="none" stroke="#fff" stroke-width="1.6"/>
          <ellipse cx="14" cy="14" rx="3" ry="7" fill="none" stroke="#fff" stroke-width="1.4"/>
          <line x1="7" y1="14" x2="21" y2="14" stroke="#fff" stroke-width="1.4"/>
        </svg>
        <span>Contato@exemplo.com<br>www.exemplo.com.br</span>
      </li>
      <li class="contact-item is-phone">
        <svg class="contact-icon" viewBox="0 0 28 28" aria-hidden="true">
          <circle cx="14" cy="14" r="14" fill="var(--accent)"/>
          <path d="M7 12 Q14 6 21 12 L19 14 L17 12 L11 12 L9 14 Z" fill="#fff"/>
          <rect x="9" y="14" width="10" height="7" rx="1.5" fill="#fff"/>
        </svg>
        <span>(00) 9999-0000<br>(00) 9999-0000</span>
      </li>
      <li class="contact-item is-place">
        <svg class="contact-icon" viewBox="0 0 28 28" aria-hidden="true">
          <circle cx="14" cy="14" r="14" fill="var(--accent)"/>
          <path d="M14 6 C10 6 8.5 9 8.5 11.5 C8.5 15 14 21 14 21 C14 21 19.5 15 19.5 11.5 C19.5 9 18 6 14 6 Z" fill="#fff"/>
          <circle cx="14" cy="11.5" r="2.2" fill="var(--accent)"/>
        </svg>
        <span>Rua exemplo, Rio de Janeiro - RJ</span>
      </li>
    </ul>

    <div class="brand-name"><span class="brand-mark"></span>Rafael Moreira</div>
  </section>

</main>
</body>
</html>
```